Bakery Needs Packaging Design for Gourmet Sandwich Cookie

Packaging design will be for sandwich cookies to be wrapped individually for sale. Our product is a premium sandwich cookie, with a dulce-de-leche (caramel-colored) filling. The cookie is topped with a white coating of powdered sugar. Dessert has Peruvian origin, however do not want to explicitly use red and white (Peruvian flag colors). The design should evoke the luxurious nature of our dessert and complement well with our product's' colors. Would like to see a gold/caramel color predominantly. Please see attached for image of product we took (own).
Updates

Reason: Did not give ample time to suggest revisions.

Target Market(s)

As our product is a gourmet product, it should reach those willing to spend a premium for quality and taste.

Industry/Entity Type

Bakery

Font styles to use
Script

Requirements
Must have
• Image of our product (see attachments), either one or two cookies, whichever is best applicable to design.
• Name of our Company = Ventoras (NOT Ramoncho)
• "Gourmet Alfajores" is the name of this particular product
• "est. 1996" somewhere on the label.
Nice to have
• Please see our draft in the attachment. This is simply an inspiration. Please feel free to suggest improvements to this design, or submit a completely new, unique one. We are seeking combinations of colors that pair well and emphasize the elegance of our product.
Should not have
• Although our cookie is a Peruvian cookie, it should not limit itself to red and white colors (Peruvian flag colors).
• "Ramoncho" It is not our company name anymore. It is now "Ventoras" this should be in script.
• "Alfajores Peruanos" - It should simply say "Gourmet Alfajores" should be in print (for visibility)

```html
<!DOCTYPE html>
<html lang="en">
<head>
<meta charset="utf-8">
<title>Ventoras Gourmet Alfajores Label</title>
<link rel="stylesheet" href="https://fonts.googleapis.com/css2?family=Great+Vibes&family=Nunito:wght@800&family=Tinos:wght@400;700&display=swap">
<style>
  :root {
    --cream: #fbf6ea;
    --caramel: #c98a2e;
    --caramel-deep: #8f5a17;
    --caramel-dark: #6b400d;
    --gold: #e8b84a;
    --gold-light: #f6dc8e;
    --brown: #4a2a0a;
    --ornament-soft: #f1dfb4;
    --leaf: #efe0bf;
    --cookie-light: #f3eee6;
    --cookie-mid: #dcc8a6;
    --cookie-dark: #b08c5c;
  }
  html, body { margin: 0; padding: 0; overflow: hidden; }
  body { width: 849px; height: 1200px; background: var(--cream); }
  .label {
    position: relative;
    width: 849px;
    height: 1200px;
    overflow: hidden;
    background: var(--cream);
  }
  .corner-ornament {
    position: absolute;
    left: -40px; top: -40px;
    width: 210px; height: 210px;
    border-radius: 50%;
    background: radial-gradient(circle, var(--ornament-soft) 0%, rgba(241,223,180,0) 70%);
  }
  .leaf-spray {
    position: absolute;
    left: 40px; top: 250px;
    width: 770px; height: 170px;
    background: radial-gradient(ellipse at center, var(--leaf) 0%, rgba(239,224,191,0) 70%);
  }
  .est {
    position: absolute;
    right: 32px; top: 20px;
    margin: 0;
    font-family: "Nunito", sans-serif;
    font-weight: 800;
    font-size: 40px;
    color: var(--caramel-deep);
  }
  .gold-field, .ribbon { position: absolute; left: 0; top: 0; }
  .brand-name {
    position: absolute;
    left: 0; top: 96px;
    width: 849px;
    margin: 0;
    text-align: center;
    font-family: "Great Vibes", cursive;
    font-weight: 400;
    font-size: 112px;
    line-height: 1;
    color: var(--gold-light);
  }
  .product-photo {
    position: absolute;
    left: 120px; top: 300px;
    width: 650px; height: 650px;
    border-radius: 48% 42% 40% 46% / 50% 46% 44% 50%;
    background: radial-gradient(ellipse at 45% 40%, var(--cookie-light) 0%, var(--cookie-mid) 62%, var(--cookie-dark) 100%);
  }
  .product-name {
    position: absolute;
    left: 127px; top: 962px;
    margin: 0;
    font-family: "Tinos", serif;
    font-weight: 400;
    font-size: 46px;
    line-height: 1.1;
    color: var(--cream);
  }
  .scroll-ornament {
    position: absolute;
    left: 30px; top: 1040px;
    width: 789px; height: 140px;
    border-radius: 70px 70px 12px 12px;
    background: radial-gradient(ellipse at 50% 40%, var(--gold-light) 0%, rgba(246,220,142,0.35) 45%, rgba(246,220,142,0) 75%);
  }
</style>
</head>
<body>
<div class="label">
  <div class="corner-ornament" role="img" aria-label="Soft floral mandala ornament"></div>
  <p class="est">est. 1996</p>
  <div class="leaf-spray" role="img" aria-label="Faint golden leaf sprigs"></div>

  <svg class="gold-field" width="849" height="1200" viewBox="0 0 849 1200">
    <defs>
      <linearGradient id="fieldTone" x1="0" y1="0" x2="0" y2="1">
        <stop offset="0" stop-color="#d99a3a"/>
        <stop offset="1" stop-color="#a8691f"/>
      </linearGradient>
    </defs>
    <path fill="url(#fieldTone)" d="M60 1200 L60 420 C60 370 100 340 150 340 C220 340 240 380 300 380 C360 380 380 335 424 335 C470 335 490 380 550 380 C610 380 630 340 700 340 C750 340 790 370 790 420 L790 560 C790 600 849 600 849 640 L849 1200 L0 1200 L0 640 C0 600 60 600 60 560 Z"/>
    <path fill="none" stroke="var(--gold-light)" stroke-width="3" d="M78 1185 L78 425 C78 385 110 358 150 358 C215 358 240 398 300 398 C360 398 385 353 424 353 C464 353 490 398 550 398 C610 398 635 358 700 358 C740 358 772 385 772 425 L772 565 C772 610 831 612 831 650 L831 1185 Z"/>
  </svg>

  <svg class="ribbon" width="849" height="340" viewBox="0 0 849 340">
    <path fill="var(--caramel-deep)" d="M40 170 L150 150 L150 300 L40 300 L90 235 Z"/>
    <path fill="var(--caramel-deep)" d="M809 170 L699 150 L699 300 L809 300 L759 235 Z"/>
    <path fill="var(--caramel-dark)" d="M150 270 L190 300 L190 250 Z M699 270 L659 300 L659 250 Z"/>
    <path fill="var(--caramel)" d="M150 130 C320 80 529 80 699 130 L699 270 C529 220 320 220 150 270 Z"/>
    <path fill="none" stroke="var(--gold-light)" stroke-width="3" d="M160 142 C325 96 524 96 689 142 M160 256 C325 210 524 210 689 256"/>
  </svg>
  <h1 class="brand-name">Ventoras</h1>

  <div class="product-photo" role="img" aria-label="Photo of two stacked alfajores dusted with powdered sugar, with dulce de leche filling"></div>

  <h2 class="product-name">Gourmet Alfajores</h2>

  <div class="scroll-ornament" role="img" aria-label="Golden filigree scrollwork border"></div>
</div>
</body>
</html>
```